Doctor in Veterinary Medecine/ veterinarian

I am a vet and would like a buisness card which is simple yet elegant and professional.
My aim is to help as much animals as I can. My main field of expertise are dogs and cats. I would like the card to reflect a "family doctor" feeling.
It should not be the traditional picture of a paw or a dog but yet it should have a sign of a pet on it. I would like to have my name Lina Haddoul as well as my profession D.V.M and my number.

Target Market(s)

Lebanese population who have pets

Industry/Entity Type

Doctor

Contact Information for Business Card

Should contain my profession " D.V.M", my full name "Lina Haddoul" and my number "0096171539214"

Requirements
Must have
• A certain picture depicting my profession
Nice to have
• Some sort of picture related to pets and animals
Should not have
• A picture of a paw or a dog. I need something more creative

```html
<!DOCTYPE html>
<html lang="en">
<head>
<meta charset="utf-8">
<title>Lina Haddoul D.V.M – Business Card</title>
<link rel="stylesheet" href="https://fonts.googleapis.com/css2?family=Open+Sans:wght@300;400;600;700&display=swap">
<style>
  :root {
    --page: #ffffff;
    --card: #f3f4f6;
    --ink: #111111;
    --text: #333333;
    --accent: #ee8e35;
    --slate: #6f6f6f;
    --mark-light: #f1d5b5;
    --mark-dark: #8a8a8a;
  }
  html, body {
    margin: 0;
    padding: 0;
    width: 1200px;
    height: 874px;
    overflow: hidden;
    background: var(--page);
    font-family: "Open Sans", Arial, sans-serif;
  }
  .canvas {
    position: relative;
    width: 1200px;
    height: 874px;
  }
  .card {
    position: absolute;
    left: 38px;
    top: 99px;
    width: 1140px;
    height: 683px;
    background: var(--card);
  }
  .pet-mark {
    position: absolute;
    left: 110px;
    top: 30px;
    width: 172px;
    height: 204px;
    border-radius: 40% 40% 46% 46%;
    background: linear-gradient(180deg, var(--mark-light) 0%, var(--mark-dark) 45%, var(--slate) 100%);
  }
  .identity {
    position: absolute;
    left: 94px;
    top: 350px;
    display: inline-block;
  }
  .identity__name {
    margin: 0;
    font-size: 62px;
    line-height: 1;
    color: var(--ink);
    text-transform: uppercase;
    white-space: nowrap;
  }
  .identity__first { font-weight: 300; }
  .identity__last { font-weight: 700; }
  .identity__title {
    margin: 8px 0 0;
    text-align: right;
    font-size: 27px;
    font-weight: 600;
    color: var(--accent);
    letter-spacing: 1px;
  }
  .contacts {
    position: absolute;
    right: 0;
    top: 298px;
    margin: 0;
    padding: 0;
    list-style: none;
  }
  .contact {
    display: flex;
    justify-content: flex-end;
    align-items: center;
    height: 39px;
    margin-bottom: 10px;
  }
  .contact__text {
    font-size: 28px;
    font-weight: 400;
    color: var(--text);
    margin-right: 10px;
    white-space: nowrap;
  }
  .contact__tag {
    width: 118px;
    height: 39px;
    background: var(--accent);
    display: flex;
    align-items: center;
    padding-left: 12px;
    box-sizing: border-box;
  }
  .contact__tag svg { width: 26px; height: 26px; }
  .address {
    position: absolute;
    left: 0;
    top: 609px;
    display: flex;
    align-items: center;
  }
  .address__tag {
    width: 86px;
    height: 39px;
    background: var(--slate);
    display: flex;
    justify-content: flex-end;
    align-items: center;
    padding-right: 10px;
    box-sizing: border-box;
  }
  .address__tag svg { width: 22px; height: 30px; }
  .address__text {
    margin-left: 9px;
    font-size: 24px;
    color: var(--text);
    letter-spacing: 2.9px;
    white-space: nowrap;
    text-transform: uppercase;
  }
</style>
</head>
<body>
<main class="canvas">
  <section class="card">
    <div class="pet-mark" role="img" aria-label="Practice emblem: a friendly pet head wearing an orange crown"></div>

    <div class="identity">
      <h1 class="identity__name"><span class="identity__first">Lina</span> <span class="identity__last">Haddoul</span></h1>
      <p class="identity__title">D.V.M</p>
    </div>

    <ul class="contacts">
      <li class="contact">
        <span class="contact__text">0096171539214</span>
        <span class="contact__tag">
          <svg viewBox="0 0 24 24" fill="none" stroke="#fff" stroke-width="1.4" stroke-linejoin="round" aria-hidden="true">
            <path d="M5 3h4l2 5-2.5 1.5a11 11 0 0 0 6 6L16 13l5 2v4a2 2 0 0 1-2 2A17 17 0 0 1 3 5a2 2 0 0 1 2-2z"/>
          </svg>
        </span>
      </li>
      <li class="contact">
        <span class="contact__text">COMPANY.COM</span>
        <span class="contact__tag">
          <svg viewBox="0 0 24 24" fill="none" stroke="#fff" stroke-width="1.4" aria-hidden="true">
            <circle cx="12" cy="12" r="10"/>
            <ellipse cx="12" cy="12" rx="4.5" ry="10"/>
            <path d="M2 12h20M4 7h16M4 17h16M12 2v20"/>
          </svg>
        </span>
      </li>
      <li class="contact">
        <span class="contact__text">EMAIL@ADDRESS.COM</span>
        <span class="contact__tag">
          <svg viewBox="0 0 24 24" fill="none" stroke="#fff" stroke-width="1.4" stroke-linejoin="round" aria-hidden="true">
            <rect x="2" y="5" width="20" height="14"/>
            <path d="M2 5l10 8 10-8"/>
          </svg>
        </span>
      </li>
    </ul>

    <div class="address">
      <span class="address__tag">
        <svg viewBox="0 0 22 30" fill="none" stroke="#fff" stroke-width="1.5" aria-hidden="true">
          <path d="M11 28C5 19 2 14 2 10a9 9 0 0 1 18 0c0 4-3 9-9 18z"/>
          <circle cx="11" cy="10" r="3.5"/>
        </svg>
      </span>
      <span class="address__text">It’s a very big address one line for your company’s address</span>
    </div>
  </section>
</main>
</body>
</html>
```